Change base color of existing graphics

We have an existing graphic(s) that is a border to our web page. Our client has requested a color change of the base color to 0,120,193. We do NOT have the original PSD files.

Top corners are rounded and contain corporate logos which will be sent to those with interest in the project.

This does not need to be a pixel perfect copy of the existing images, but it is the baseline they have requested so it should be similar in feel but there is some freedom in design.

The large square buttons in the screen shot are client provided and will not change.

What I would like returned are cut images identical to the attachments so they can simply be swapped out on the website. Would also like original PSD or other format that is used to generate.

Any questions, please do not hesitate to contact.

```html
<!DOCTYPE html>
<html lang="en">
<head>
<meta charset="utf-8">
<title>Weekly Report Selector</title>
<link href="https://fonts.googleapis.com/css2?family=Arimo:wght@400;700&display=swap" rel="stylesheet">
<style>
  :root {
    --page-bg: #ffffff;
    --brand-blue: #0078c1;
    --brand-blue-dark: #005a93;
    --brand-blue-light: #3f9ad6;
    --band-shine: #eaf4fb;
    --frame-edge: #c9d3da;
    --label-ink: #222222;
    --field-border: #7a7a7a;
    --field-bg: #ffffff;
    --muted-ink: #9a9a9a;
    --button-face: #f2f2f2;
    --button-border: #8c8c8c;
    --tile-glow: rgba(80, 160, 230, 0.55);
    --tile-top: #4a8fd0;
    --tile-bottom: #1c5ea8;
    --tile-mark: #ffffff;
  }
  html, body {
    margin: 0;
    padding: 0;
    width: 1200px;
    height: 900px;
    overflow: hidden;
    background: var(--page-bg);
    font-family: "Arimo", Arial, sans-serif;
  }
  .canvas {
    position: relative;
    width: 1200px;
    height: 900px;
  }
  .page-frame {
    position: absolute;
    left: 15px;
    top: 203px;
    width: 1170px;
    height: 470px;
    background: var(--page-bg);
    border: 1px solid var(--frame-edge);
    border-radius: 10px 10px 4px 4px;
    box-sizing: border-box;
    overflow: hidden;
  }
  .header-band {
    position: absolute;
    left: 0;
    top: 0;
    width: 100%;
    height: 52px;
    background:
      linear-gradient(90deg, rgba(255,255,255,0) 0px, rgba(255,255,255,0.35) 60px, var(--band-shine) 110px, rgba(255,255,255,0.3) 160px, rgba(255,255,255,0) 200px),
      linear-gradient(180deg, var(--brand-blue-light) 0%, var(--brand-blue) 45%, var(--brand-blue-dark) 100%);
    border-bottom: 4px solid #d6e3ec;
  }
  .brand-name {
    position: absolute;
    right: 30px;
    top: 16px;
    display: flex;
    align-items: center;
    gap: 6px;
    font-size: 16px;
    font-weight: 400;
    color: #1a1a1a;
    background: rgba(255,255,255,0.85);
    padding: 2px 8px;
    border-radius: 3px;
  }
  .brand-dot {
    width: 10px;
    height: 10px;
    border-radius: 50%;
    background: var(--brand-blue);
  }
  .footer-band {
    position: absolute;
    left: 0;
    bottom: 0;
    width: 100%;
    height: 16px;
    background: linear-gradient(180deg, var(--brand-blue-light), var(--brand-blue-dark));
    border-top: 3px solid #d6e3ec;
  }
  .filter-form {
    position: absolute;
    left: 380px;
    top: 120px;
    font-size: 11px;
    color: var(--label-ink);
  }
  .filter-row {
    display: flex;
    align-items: center;
    height: 30px;
  }
  .filter-label {
    width: 97px;
    text-align: right;
    padding-right: 12px;
  }
  .filter-select {
    height: 15px;
    border: 1px solid var(--field-border);
    background: var(--field-bg);
    font-size: 10px;
    display: flex;
    align-items: center;
    justify-content: space-between;
    padding-left: 3px;
    box-sizing: border-box;
  }
  .filter-select .arrow {
    width: 10px;
    height: 13px;
    border-left: 1px solid var(--field-border);
    background: #e8e8e8;
    position: relative;
  }
  .filter-select .arrow::after {
    content: "";
    position: absolute;
    left: 2px;
    top: 5px;
    border-left: 3px solid transparent;
    border-right: 3px solid transparent;
    border-top: 4px solid #333;
  }
  .select-level { width: 61px; }
  .select-unit { width: 193px; color: var(--muted-ink); }
  .select-week { width: 124px; }
  .action-tile {
    position: absolute;
    top: 242px;
    width: 136px;
    height: 127px;
    border-radius: 12px;
    background: linear-gradient(180deg, var(--tile-top) 0%, #2f74bd 50%, var(--tile-bottom) 100%);
    border: 3px solid #8fc0ea;
    box-sizing: border-box;
    box-shadow: 0 0 22px 10px var(--tile-glow);
  }
  .action-tile .tile-art {
    position: absolute;
    left: 18px;
    top: 16px;
    width: 94px;
    height: 90px;
    border-radius: 8px;
    background: linear-gradient(135deg, rgba(255,255,255,0.25), rgba(255,255,255,0.05));
  }
  .tile-one { left: 325px; }
  .tile-two { left: 517px; }
  .tile-three { left: 710px; }
  .page-actions {
    position: absolute;
    top: 424px;
    left: 471px;
    display: flex;
    gap: 16px;
  }
  .page-button {
    height: 15px;
    font-size: 9px;
    font-family: "Arimo", Arial, sans-serif;
    color: #111;
    background: linear-gradient(180deg, #ffffff, var(--button-face));
    border: 1px solid var(--button-border);
    border-radius: 2px;
    padding: 0 5px;
    line-height: 13px;
  }
  .page-button.is-disabled { color: var(--muted-ink); width: 84px; }
</style>
</head>
<body>
<div class="canvas">
  <div class="page-frame">
    <header class="header-band">
      <div class="brand-name"><span>Lookout Metrics</span><span class="brand-dot"></span></div>
    </header>

    <form class="filter-form">
      <div class="filter-row">
        <span class="filter-label">Select Level:</span>
        <span class="filter-select select-level"><span>Store</span><span class="arrow"></span></span>
      </div>
      <div class="filter-row">
        <span class="filter-label">Select Unit:</span>
        <span class="filter-select select-unit"><span>Main Street Unit</span><span class="arrow"></span></span>
      </div>
      <div class="filter-row">
        <span class="filter-label">Select Week:</span>
        <span class="filter-select select-week"><span>December Week 2 2013</span><span class="arrow"></span></span>
      </div>
    </form>

    <div class="action-tile tile-one"><div class="tile-art" role="img" aria-label="Client-provided button icon"></div></div>
    <div class="action-tile tile-two"><div class="tile-art" role="img" aria-label="Client-provided button icon"></div></div>
    <div class="action-tile tile-three"><div class="tile-art" role="img" aria-label="Client-provided button icon"></div></div>

    <div class="page-actions">
      <span class="page-button">Take Survey</span>
      <span class="page-button">Archives</span>
      <span class="page-button is-disabled">Print Report</span>
    </div>

    <footer class="footer-band"></footer>
  </div>
</div>
</body>
</html>
```